Business Card Design Project

We would like you to create business cards. The color scheme should match our website and logo. I have attached an image of a page of our website, as well as our logo. Please Please include the logo on the left with a similar faded horizontal line, and a blueprint type sketch of a house on cribbing on the right, similar to our website. We like the idea of how this looks. I have attached a third image of an actual house on cribbing (crisscrossed wooden beams). Please include cribbing in the blueprint type sketch.

The information to be included on the business cards is

(name)
214 Alder Lane
Suite 317
Harlow Springs, NJ 07815
908.641.2093
www.brickwardliftworks.com
info@brickwardliftworks.com

This information can be spaced in any way.

I will also be posting a job for letterhead using the same design as the business cards.

If you need anything other information or I have not been clear enough, please do not hesitate to message me.

Thank you!
Updates

This design project is now open to all designers.  Please message me with any questions.  Thank you.

Industry/Entity Type

House

Requirements
Must have
• 1. Our logo
2. Blueprint type sketch of a house on wooden cribbing.
3. Color scheme to match logo and website.
4. Information provided.

```html
<!DOCTYPE html>
<html lang="en">
<head>
<meta charset="utf-8">
<title>Brickward Liftworks – Business Card</title>
<link rel="stylesheet" href="https://fonts.googleapis.com/css2?family=Questrial&display=swap">
<style>
  :root {
    --page-bg: #e6e6e6;
    --card-black: #151515;
    --card-black-soft: #1d1d1d;
    --silver-light: #f2f2f2;
    --silver-mid: #b9b9b9;
    --silver-dark: #5e5e5e;
    --accent-orange: #f0961e;
    --text-light: #e8e8e8;
    --text-muted: #c9c9c9;
    --blueprint-navy: #23246a;
    --blueprint-blue: #2f3c8c;
  }
  * { margin: 0; padding: 0; box-sizing: border-box; }
  html, body { width: 1200px; height: 900px; overflow: hidden; }
  body {
    background: var(--page-bg);
    font-family: "Questrial", "Century Gothic", sans-serif;
    position: relative;
  }
  .card {
    position: absolute;
    left: 290px;
    width: 620px;
    height: 354px;
    border-radius: 18px;
    overflow: hidden;
    box-shadow: 0 10px 26px rgba(0,0,0,.35);
  }
  .metal {
    background: linear-gradient(100deg, var(--silver-dark) 0%, var(--silver-mid) 22%, var(--silver-light) 40%, var(--silver-mid) 55%, var(--silver-dark) 75%, var(--silver-mid) 100%);
  }

  /* Back side */
  .card-back { top: 60px; }
  .card-back .band-top, .card-back .band-bottom { position: absolute; left: 0; right: 0; height: 72px; }
  .card-back .band-top { top: 0; }
  .card-back .band-bottom { bottom: 0; }
  .card-back .band-center {
    position: absolute; top: 72px; bottom: 72px; left: 0; right: 0;
    background: linear-gradient(180deg, #0c0c0c, var(--card-black-soft) 50%, #0c0c0c);
    display: flex; align-items: center; justify-content: center;
  }

  .brand { display: flex; flex-direction: column; align-items: center; gap: 8px; }
  .brand-row { display: flex; align-items: center; gap: 10px; }
  .brand-mark { width: 14px; height: 14px; background: var(--accent-orange); }
  .brand-name { color: var(--text-light); font-size: 30px; letter-spacing: 1px; }
  .brand-tagline { color: var(--accent-orange); font-size: 11px; letter-spacing: .5px; }

  /* Front side */
  .card-front { top: 486px; background: var(--card-black); }
  .card-front .edge-top, .card-front .edge-bottom { position: absolute; left: 0; right: 0; height: 14px; z-index: 2; }
  .card-front .edge-top { top: 0; }
  .card-front .edge-bottom { bottom: 0; }
  .blueprint {
    position: absolute; top: 0; right: 0; bottom: 0; width: 380px;
    background: linear-gradient(90deg, rgba(21,21,21,1) 0%, rgba(35,36,106,.55) 40%, var(--blueprint-navy) 75%, var(--blueprint-blue) 100%);
  }
  .front-content { position: absolute; left: 40px; top: 40px; z-index: 1; }
  .front-content .brand { align-items: flex-start; }
  .front-content .brand-name { font-size: 26px; }
  .person { margin: 26px 0 0 40px; }
  .person-name { color: var(--text-light); font-size: 21px; }
  .person-role { color: var(--accent-orange); font-size: 12px; margin-top: 3px; }
  .contact { list-style: none; margin-top: 26px; }
  .contact li { display: flex; align-items: center; gap: 10px; color: var(--text-muted); font-size: 14px; line-height: 25px; white-space: nowrap; }
  .contact svg { width: 13px; height: 13px; fill: var(--accent-orange); flex: none; }
</style>
</head>
<body>

<section class="card card-back" aria-label="Business card back">
  <div class="band-top metal"></div>
  <div class="band-center">
    <div class="brand">
      <div class="brand-row">
        <span class="brand-mark"></span>
        <span class="brand-name">Brickward Liftworks</span>
      </div>
      <span class="brand-tagline">House Raising Construction Masonry</span>
    </div>
  </div>
  <div class="band-bottom metal"></div>
</section>

<section class="card card-front" aria-label="Business card front">
  <div class="edge-top metal"></div>
  <div class="blueprint" role="img" aria-label="Blueprint-style line sketch of a house raised on wooden cribbing"></div>
  <div class="front-content">
    <div class="brand">
      <div class="brand-row">
        <span class="brand-mark"></span>
        <span class="brand-name">Brickward Liftworks</span>
      </div>
      <span class="brand-tagline">House Raising Construction Masonry</span>
    </div>
    <div class="person">
      <div class="person-name">Dana Whitlock</div>
      <div class="person-role">general manager</div>
    </div>
    <ul class="contact">
      <li><svg viewBox="0 0 16 16"><path d="M3 1l3 3-2 2c1 2 3 4 5 5l2-2 3 3-2 3C7 15 1 9 1 3z"/></svg>908.641.2093</li>
      <li><svg viewBox="0 0 16 16"><path d="M8 1a7 7 0 1 0 4 12.7l-.8-1.2A5.5 5.5 0 1 1 13.5 8v1a1.3 1.3 0 0 1-2.6 0V5h-1.3v.6A3 3 0 1 0 10 10.6 2.7 2.7 0 0 0 15 9V8a7 7 0 0 0-7-7zm0 8.6A1.6 1.6 0 1 1 8 6.4a1.6 1.6 0 0 1 0 3.2z"/></svg>info@brickwardliftworks.com</li>
      <li><svg viewBox="0 0 16 16"><path d="M8 1a7 7 0 1 0 0 14A7 7 0 0 0 8 1zm0 1.5c.9 0 1.9 1.8 2.2 4.5H5.8C6.1 4.3 7.1 2.5 8 2.5zM2.6 7.2h1.9c0 .3 0 .5 0 .8 0 .3 0 .6 0 .8H2.6a5.5 5.5 0 0 1 0-1.6zm3.2 1.6V8c0-.3 0-.5 0-.8h4.4v1.6H5.8zm5.7 0v-1.6h1.9a5.5 5.5 0 0 1 0 1.6h-1.9zM8 13.5c-.9 0-1.9-1.8-2.2-4.5h4.4c-.3 2.7-1.3 4.5-2.2 4.5z"/></svg>www.brickwardliftworks.com</li>
      <li><svg viewBox="0 0 16 16"><path d="M8 1L1 7.5h2V15h4v-4h2v4h4V7.5h2z"/></svg>214 Alder Lane Suite 317 Harlow Springs, NJ 07815</li>
    </ul>
  </div>
  <div class="edge-bottom metal"></div>
</section>

</body>
</html>
```